Cosmetic Clinic Looking For Sign Designs

We are looking for sign design ideas for the front of our building and a lawn sign for our cosmetic injection salon.
I have uploaded the front of our building for a mock up and size, lawn posts with size and a sign that uses the same dimensions.
We would like both signs to be black for the background.

Target Market(s)

Ages 18-75

Industry/Entity Type

Beauty

Requirements
Must have
• Services we offer:
• Cosmetic Injections
• Airbrush Spray Tanning
• Eyelash Growth Serum
• Skin Care Products & More
• Everything must be on a black background
• The lawn sign must have the address: 394 Fenwick and the building sign should have the phone number.
Should not have
• Nothing can light up (no LED)
• Both signs do not need the full address. Just 394 Fenwick and the phone number

```html
<!DOCTYPE html>
<html lang="en">
<head>
<meta charset="utf-8">
<title>Velvet Hour Salon – Sign Designs</title>
<link rel="stylesheet" href="https://fonts.googleapis.com/css2?family=Fira+Sans+Condensed:wght@600&family=Rubik:ital,wght@0,700;1,800&display=swap">
<style>
  :root {
    --board: #4a4a4a;
    --black: #000000;
    --white: #ffffff;
    --teal: #1f9bb8;
    --pink: #ec1b7f;
    --violet: #7b7fc4;
  }
  html, body {
    margin: 0;
    padding: 0;
    width: 1200px;
    height: 848px;
    overflow: hidden;
    background: var(--board);
  }
  .artboard {
    position: relative;
    width: 1200px;
    height: 848px;
  }
  .sign {
    position: absolute;
    display: block;
  }
  .building-sign { left: 62px; top: 54px; }
  .lawn-sign { left: 401px; top: 333px; }
  .brand-name {
    font-family: "Fira Sans Condensed", "Arial Narrow", sans-serif;
    font-weight: 600;
    fill: var(--teal);
  }
  .services-title,
  .service-item {
    font-family: "Rubik", "Arial Black", sans-serif;
    font-weight: 800;
    font-style: italic;
    fill: var(--white);
  }
  .bullet { fill: var(--white); }
  .phone,
  .address {
    font-family: "Rubik", "Arial", sans-serif;
    font-weight: 700;
    fill: var(--white);
  }
  .address-lawn { fill: var(--pink); }
  .text-shadow { filter: url(#softShadow); }
</style>
</head>
<body>
<main class="artboard">

  <svg width="0" height="0" style="position:absolute" aria-hidden="true">
    <defs>
      <linearGradient id="silkBackground" x1="0" y1="0" x2="1" y2="1">
        <stop offset="0" stop-color="#0a0a0a"/>
        <stop offset="0.35" stop-color="#2a2a2a"/>
        <stop offset="0.5" stop-color="#121212"/>
        <stop offset="0.7" stop-color="#333333"/>
        <stop offset="1" stop-color="#0c0c0c"/>
      </linearGradient>
      <linearGradient id="ringGradient" x1="0" y1="0" x2="1" y2="0">
        <stop offset="0" stop-color="#7b7fc4"/>
        <stop offset="0.45" stop-color="#c45aa8"/>
        <stop offset="0.85" stop-color="#ec1b7f"/>
        <stop offset="1" stop-color="#f7b7d6"/>
      </linearGradient>
      <linearGradient id="ringGradientLawn" x1="0" y1="0" x2="0" y2="1">
        <stop offset="0" stop-color="#a48fd0"/>
        <stop offset="0.6" stop-color="#ec1b7f"/>
        <stop offset="1" stop-color="#7b7fc4"/>
      </linearGradient>
      <linearGradient id="phoneBand" x1="0" y1="0" x2="0" y2="1">
        <stop offset="0" stop-color="#ec1b7f"/>
        <stop offset="1" stop-color="#a00f55"/>
      </linearGradient>
      <filter id="softShadow" x="-5%" y="-20%" width="110%" height="150%">
        <feDropShadow dx="1.5" dy="2" stdDeviation="1.2" flood-color="#000" flood-opacity="0.85"/>
      </filter>
    </defs>
  </svg>

  <!-- Building front sign -->
  <svg class="sign building-sign" width="1077" height="244" viewBox="0 0 1077 244" role="group" aria-label="Building sign">
    <rect class="sign-background" width="1077" height="244" fill="url(#silkBackground)"/>
    <path class="silk-streak" d="M420 244 C600 150 800 120 1077 40" stroke="#444" stroke-width="30" fill="none" opacity="0.35"/>
    <path class="silk-streak" d="M480 244 C700 190 880 170 1077 130" stroke="#3a3a3a" stroke-width="18" fill="none" opacity="0.35"/>

    <circle class="brand-disc" cx="251" cy="121" r="212" fill="var(--black)"/>
    <circle class="brand-ring" cx="251" cy="121" r="212" fill="none" stroke="url(#ringGradient)" stroke-width="8"/>

    <circle class="brand-circle" cx="251" cy="73" r="56" fill="var(--violet)"/>
    <text class="brand-name" x="251" y="196" text-anchor="middle" font-size="50" textLength="284" lengthAdjust="spacing">VELVET HOUR</text>
    <text class="brand-name" x="251" y="228" text-anchor="middle" font-size="28" letter-spacing="2">SALON</text>

    <g class="text-shadow">
      <text class="services-title" x="493" y="45" font-size="30">Services we offer:</text>
      <text class="phone phone-building" x="1055" y="45" text-anchor="end" font-size="24" textLength="178" lengthAdjust="spacing">(555) 014-2278</text>
      <circle class="bullet" cx="576" cy="80" r="4.5"/>
      <text class="service-item" x="598" y="91" font-size="29" textLength="310" lengthAdjust="spacing">Cosmetic Injections</text>
      <circle class="bullet" cx="576" cy="119" r="4.5"/>
      <text class="service-item" x="598" y="130" font-size="29" textLength="362" lengthAdjust="spacing">Airbrush Spray Tanning</text>
      <circle class="bullet" cx="576" cy="158" r="4.5"/>
      <text class="service-item" x="598" y="169" font-size="29" textLength="350" lengthAdjust="spacing">Eyelash Growth Serum</text>
      <circle class="bullet" cx="576" cy="197" r="4.5"/>
      <text class="service-item" x="598" y="208" font-size="29" textLength="424" lengthAdjust="spacing">Skin Care Products &amp; More</text>
    </g>
  </svg>

  <!-- Lawn sign -->
  <svg class="sign lawn-sign" width="398" height="498" viewBox="0 0 398 498" role="group" aria-label="Lawn sign">
    <rect class="sign-background" width="398" height="498" fill="url(#silkBackground)"/>
    <path class="silk-streak" d="M0 300 C120 230 260 200 398 120" stroke="#444" stroke-width="26" fill="none" opacity="0.3"/>

    <circle class="brand-disc" cx="199" cy="58" r="172" fill="var(--black)"/>
    <circle class="brand-ring" cx="199" cy="58" r="172" fill="none" stroke="url(#ringGradientLawn)" stroke-width="7"/>

    <circle class="brand-circle" cx="199" cy="50" r="42" fill="var(--violet)"/>
    <text class="brand-name" x="199" y="145" text-anchor="middle" font-size="41" textLength="228" lengthAdjust="spacing">VELVET HOUR</text>
    <text class="brand-name" x="199" y="172" text-anchor="middle" font-size="23" letter-spacing="2">SALON</text>
    <text class="address address-lawn" x="199" y="206" text-anchor="middle" font-size="19" letter-spacing="0.5">394 Fenwick</text>

    <g class="text-shadow">
      <text class="services-title" x="199" y="279" text-anchor="middle" font-size="27" textLength="254" lengthAdjust="spacing">Services we offer</text>
      <circle class="bullet" cx="39" cy="315" r="3.8"/>
      <text class="service-item" x="54" y="322" font-size="21" textLength="228" lengthAdjust="spacing">Cosmetic Injections</text>
      <circle class="bullet" cx="39" cy="344" r="3.8"/>
      <text class="service-item" x="54" y="351" font-size="21" textLength="266" lengthAdjust="spacing">Airbrush Spray Tanning</text>
      <circle class="bullet" cx="39" cy="373" r="3.8"/>
      <text class="service-item" x="54" y="380" font-size="21" textLength="257" lengthAdjust="spacing">Eyelash Growth Serum</text>
      <circle class="bullet" cx="39" cy="402" r="3.8"/>
      <text class="service-item" x="54" y="409" font-size="21" textLength="311" lengthAdjust="spacing">Skin Care Products &amp; More</text>
    </g>

    <path class="phone-band-edge" d="M0 445 Q199 420 398 445 L398 498 L0 498 Z" fill="var(--violet)"/>
    <path class="phone-band" d="M0 452 Q199 426 398 452 L398 498 L0 498 Z" fill="url(#phoneBand)"/>
    <text class="phone text-shadow" x="199" y="483" text-anchor="middle" font-size="31" textLength="252" lengthAdjust="spacing">(555) 014-2278</text>
  </svg>

</main>
</body>
</html>
```